Commercial Construction Company

We need a business card design based on our current logo. We are a commercial general contractor based in Southern California that specializes in bank remodels. We would like to see designs that incorporate dark blue. The final design should portray an image of professionalism and quality.

If possible, I would like to add metallic foil to the design. Thank you

```html
<!DOCTYPE html>
<html lang="en">
<head>
<meta charset="utf-8">
<title>Halvorsen Builders – Business Card</title>
<link href="https://fonts.googleapis.com/css2?family=Open+Sans:wght@400;600;700&display=swap" rel="stylesheet">
<style>
  :root {
    --page: #e9e7e4;
    --card-black: #0b0c0e;
    --texture-dark: #1c1d20;
    --texture-mid: #2c2d31;
    --navy: #1b5597;
    --silver-light: #f2f2f2;
    --silver-mid: #bfc1c4;
    --silver-dark: #7d8084;
    --text: #f4f4f4;
  }
  * { margin: 0; padding: 0; box-sizing: border-box; }
  html, body {
    width: 1200px; height: 909px; overflow: hidden;
    background: var(--page);
    font-family: "Open Sans", Arial, sans-serif;
  }
  .canvas {
    position: relative; width: 1200px; height: 909px;
    display: flex; flex-direction: column; align-items: center; justify-content: center; gap: 34px;
  }
  .card {
    position: relative; width: 700px; height: 400px; overflow: hidden;
    background: var(--card-black);
    box-shadow: 0 10px 24px rgba(0,0,0,.28);
  }
  .card-front {
    background: radial-gradient(ellipse at 50% 45%, var(--texture-mid), var(--texture-dark) 70%, #131416);
  }
  .brand {
    position: absolute; left: 50%; top: 50%; transform: translate(-50%, -50%);
    display: flex; align-items: center; gap: 16px;
  }
  .brand-dot {
    width: 30px; height: 30px; border-radius: 50%; background: var(--navy);
  }
  .brand-name {
    font-weight: 600; font-size: 40px; letter-spacing: 1px; color: var(--silver-mid);
  }
  .card-back svg.sweep { position: absolute; inset: 0; }
  .card-back .brand { left: 555px; top: 150px; }
  .card-back .brand-name { font-size: 26px; }
  .card-back .brand-dot { width: 22px; height: 22px; }
  .name-tab {
    position: absolute; left: 0; top: 95px; width: 20px; height: 52px; background: var(--navy);
  }
  .identity { position: absolute; left: 58px; top: 82px; color: var(--text); }
  .person-name { font-weight: 700; font-size: 24px; letter-spacing: .5px; text-transform: uppercase; }
  .person-role { font-size: 17px; text-transform: uppercase; margin-top: 2px; }
  .address { position: absolute; left: 58px; top: 178px; color: var(--text); font-size: 17px; line-height: 1.35; }
  .contacts { position: absolute; left: 58px; top: 262px; list-style: none; color: var(--text); font-size: 16px; }
  .contacts li { display: flex; align-items: center; gap: 12px; height: 27px; }
  .icon {
    width: 18px; height: 18px; border-radius: 3px; background: var(--navy);
    display: flex; align-items: center; justify-content: center;
  }
  .icon svg { width: 12px; height: 12px; }
</style>
</head>
<body>
<main class="canvas">

  <section class="card card-front" aria-label="Card front">
    <div class="brand">
      <span class="brand-dot"></span>
      <span class="brand-name">Halvorsen Builders</span>
    </div>
  </section>

  <section class="card card-back" aria-label="Card back">
    <svg class="sweep" viewBox="0 0 700 400" width="700" height="400">
      <defs>
        <radialGradient id="texture" cx="75%" cy="35%" r="60%">
          <stop offset="0" stop-color="#34353a"/>
          <stop offset="1" stop-color="#18191c"/>
        </radialGradient>
        <linearGradient id="foil" x1="0" y1="0" x2="1" y2="1">
          <stop offset="0" stop-color="#8a8d91"/>
          <stop offset=".35" stop-color="#f4f4f4"/>
          <stop offset=".6" stop-color="#9c9fa3"/>
          <stop offset="1" stop-color="#e6e6e6"/>
        </linearGradient>
      </defs>
      <path d="M418 0 Q455 285 700 372 L700 0 Z" fill="url(#texture)" role="img" aria-label="Perforated dark metal texture panel"/>
      <path d="M385 0 Q405 270 620 400" fill="none" stroke="url(#foil)" stroke-width="14"/>
      <path d="M418 0 Q455 285 700 372" fill="none" stroke="var(--navy)" stroke-width="10"/>
    </svg>

    <div class="brand">
      <span class="brand-dot"></span>
      <span class="brand-name">Halvorsen Builders</span>
    </div>

    <span class="name-tab"></span>
    <div class="identity">
      <p class="person-name">Marcus Ellery</p>
      <p class="person-role">Founder/CEO</p>
    </div>
    <p class="address">218 Harbor Crest Avenue<br>Long Beach, CA 90802</p>

    <ul class="contacts">
      <li><span class="icon"><svg viewBox="0 0 12 12"><path d="M2 1h3l1 3-2 1a6 6 0 0 0 3 3l1-2 3 1v3c-6 0-9-3-9-9z" fill="#fff"/></svg></span>555-214-7730</li>
      <li><span class="icon"><svg viewBox="0 0 12 12"><path d="M2 1h3l1 3-2 1a6 6 0 0 0 3 3l1-2 3 1v3c-6 0-9-3-9-9z" fill="#fff"/></svg></span>(office) 555-214-7788</li>
      <li><span class="icon"><svg viewBox="0 0 12 12"><rect x="1" y="2.5" width="10" height="7" fill="none" stroke="#fff"/><path d="M1 2.5l5 4 5-4" fill="none" stroke="#fff"/></svg></span>marcus@halvorsenbuilders.com</li>
      <li><span class="icon"><svg viewBox="0 0 12 12"><circle cx="6" cy="6" r="4.5" fill="none" stroke="#fff"/><path d="M1.5 6h9M6 1.5c-2 2.5-2 6.5 0 9M6 1.5c2 2.5 2 6.5 0 9" fill="none" stroke="#fff" stroke-width=".8"/></svg></span>www.halvorsenbuilders.com</li>
    </ul>
  </section>

</main>
</body>
</html>
```